Crestline Marketing Business Card

Business card using new logo for marketing consulting company based in Silicon Valley. Limited information on card now (name, phone number, email, website), but room to add mailing address later.

```html
<!DOCTYPE html>
<html lang="en">
<head>
<meta charset="utf-8">
<title>Crestline Marketing – Business Card</title>
<link rel="stylesheet" href="https://fonts.googleapis.com/css2?family=Roboto+Condensed:wght@400;700&display=swap">
<style>
  :root {
    --page-bg: #ecebe8;
    --card-white: #ffffff;
    --brand-sky: #2bb3ea;
    --band-blue-light: #29a9e8;
    --band-blue-deep: #0a6fc4;
    --curve-purple: #4b2d91;
    --text-light: #ffffff;
    --card-shadow: 0 10px 28px rgba(0,0,0,.22);
  }
  * { box-sizing: border-box; margin: 0; padding: 0; }
  html, body {
    width: 1200px; height: 913px; overflow: hidden;
    background: var(--page-bg);
    font-family: "Roboto Condensed", Arial, sans-serif;
  }
  .canvas { position: relative; width: 1200px; height: 913px; }

  .card {
    position: absolute;
    width: 540px; height: 308px;
    background: var(--card-white);
    border-radius: 3px;
    box-shadow: var(--card-shadow);
    overflow: hidden;
  }
  .card--front { left: 50px; top: 130px; }
  .card--back  { left: 610px; top: 470px; }

  .wordmark {
    position: absolute;
    display: flex; align-items: center; gap: 12px;
    color: var(--brand-sky);
    font-weight: 400;
    text-transform: uppercase;
    letter-spacing: 1px;
    line-height: 1.05;
    z-index: 1;
  }
  .wordmark__dot { flex: none; border-radius: 50%; background: var(--brand-sky); }
  .card--front .wordmark { left: 50%; top: 50%; transform: translate(-50%, -50%); font-size: 38px; }
  .card--front .wordmark__dot { width: 58px; height: 58px; }
  .card--back .wordmark { right: 40px; top: 24px; font-size: 22px; }
  .card--back .wordmark__dot { width: 34px; height: 34px; }
  .wordmark__line { display: block; }

  .back__band { position: absolute; inset: 0; }

  .person {
    position: absolute; right: 36px; top: 124px;
    text-align: right; color: var(--text-light);
    z-index: 1;
  }
  .person__name { font-size: 19px; font-weight: 700; }
  .person__title { font-size: 12px; font-weight: 400; margin-top: 2px; }

  .contact-list {
    position: absolute; left: 34px; bottom: 22px;
    list-style: none; color: var(--text-light);
    font-size: 13.5px; line-height: 1.25;
    z-index: 1;
  }
  .contact-list li { display: flex; align-items: flex-start; gap: 10px; margin-top: 4px; }
  .contact-list svg { flex: none; width: 14px; height: 14px; margin-top: 1px; fill: var(--text-light); }
</style>
</head>
<body>
<main class="canvas">

  <section class="card card--front" aria-label="Card front">
    <div class="wordmark">
      <span class="wordmark__dot"></span>
      <span><span class="wordmark__line">Crestline</span><span class="wordmark__line">Marketing</span></span>
    </div>
  </section>

  <section class="card card--back" aria-label="Card back">
    <svg class="back__band" viewBox="0 0 540 308" preserveAspectRatio="none" aria-hidden="true">
      <defs>
        <linearGradient id="bandGradient" x1="0" y1="1" x2="1" y2="0">
          <stop offset="0" stop-color="#0a6fc4"/>
          <stop offset="1" stop-color="#29a9e8"/>
        </linearGradient>
      </defs>
      <path d="M0,40 Q300,170 540,95 L540,308 L0,308 Z" fill="url(#bandGradient)"/>
      <path d="M0,36 Q300,162 540,88" fill="none" stroke="#4b2d91" stroke-width="6"/>
      <path d="M0,42 Q300,170 540,97" fill="none" stroke="#ffffff" stroke-width="3"/>
    </svg>

    <div class="wordmark">
      <span class="wordmark__dot"></span>
      <span><span class="wordmark__line">Crestline</span><span class="wordmark__line">Marketing</span></span>
    </div>

    <div class="person">
      <p class="person__name">Your Name</p>
      <p class="person__title">Title</p>
    </div>

    <ul class="contact-list">
      <li>
        <svg viewBox="0 0 14 14"><path d="M7 0a5 5 0 0 0-5 5c0 3.6 5 9 5 9s5-5.4 5-9a5 5 0 0 0-5-5zm0 7a2 2 0 1 1 0-4 2 2 0 0 1 0 4z"/></svg>
        <span>Your Commercial or<br>office address</span>
      </li>
      <li>
        <svg viewBox="0 0 14 14"><path d="M3 1l2.5 3-1.5 1.5a8 8 0 0 0 4.5 4.5L10 8.5l3 2.5-1.5 2.5C6 13 1 8 .5 2.5z"/></svg>
        <span>00.00.00.0000</span>
      </li>
      <li>
        <svg viewBox="0 0 14 14"><path d="M3 1h8v4H3zM1 6h12v6h-2v-2H3v2H1zm3 5h6v3H4z"/></svg>
        <span>00.00.00.0000</span>
      </li>
      <li>
        <svg viewBox="0 0 14 14"><path d="M0 3h14v8H0zm1 1l6 4 6-4v-.2H1z" fill-rule="evenodd"/></svg>
        <span>yourname@yourwebsite.com</span>
      </li>
      <li>
        <svg viewBox="0 0 14 14"><path d="M7 0a7 7 0 1 0 0 14A7 7 0 0 0 7 0zm0 1.3c.8.9 1.4 2.6 1.5 4.7h-3C5.6 3.9 6.2 2.2 7 1.3zM1.3 8h2.9c.1 1.7.5 3.2 1.1 4.2A5.8 5.8 0 0 1 1.3 8zm0-2a5.8 5.8 0 0 1 4-4.2C4.7 2.8 4.3 4.3 4.2 6zm4.2 2h3c-.1 2-.7 3.8-1.5 4.7C6.2 11.8 5.6 10 5.5 8zm3.2 4.2c.6-1 1-2.5 1.1-4.2h2.9a5.8 5.8 0 0 1-4 4.2zM9.8 6c-.1-1.7-.5-3.2-1.1-4.2a5.8 5.8 0 0 1 4 4.2z"/></svg>
        <span>www.yourwebsite.com</span>
      </li>
    </ul>
  </section>

</main>
</body>
</html>
```